Realtor / Real Estate Lead Generation site

Need a website design for lead generation. This website connects realtors with buyers and sellers of homes. some sites i like are: lumoquest.com, brixvale.com, quillmerows.com. Those sites look nice and have the same purpose as mine. The name of my site is VelnorHomeBridge. Basically I connect people with Top producing real estate agents
Updates

Project Deadline Extended Reason: Im still waiting on all my friends to pick the design. I have sent them the link to view and comment. I will be committing payment as well. Added Monday, February 15, 2016

Target Market(s)

people looking to buy or sell a home

Industry/Entity Type

Real Estate

Coding

Coded - Design and coding required

Number of Pages Required

5+ page

Font styles to use
Sans Serif

Requirements
Must have
• 2 versions of a lead capture form. One for buyers and one for sellers. goto www.quillmerows.com and select "buyer", you will see a for asking for Price Range, Type of Home, and City or Zipcode. If you select seller it has a differnt set of questions. I like the way they have trust builders on the right hand side such as realtors faces and comments about the realtors.I would like trust builders above the fold as well, so when its viewed on a phone or computer they can see them without scrolling, something such as #1 company, please see lumoquest-mobile.png file attached. I also have an explainer video that I would like a link to on the homepage above the fold without scrolling. please see darvikto.png file to see an example. I will upload video later. There should be a thank you page, privacy policy, terms and conditions. For ALL content see. www.789plotvista.com which is my current site.
• I would like the page to be mobile responsive/wordpress. Lastly, please see the form on 789plotvista.com. once you select the city, zipcode or address, and click "find my perfect agent, a form will come up with several different sets of questions. I would like that exact form used as I already paid for it on my other site. Thank you

```html
<!DOCTYPE html>
<html lang="en">
<head>
<meta charset="UTF-8">
<title>Seller's Corner</title>
<link href="https://fonts.googleapis.com/css2?family=ABeeZee&display=swap" rel="stylesheet">
<style>
  :root {
    --mauve-dark: #8b6f79;
    --pink-hero: #ddb3c3;
    --pink-deep: #bd97a3;
    --grey-body: #e3e3e3;
    --button-berry: #a06479;
    --button-lip: #dfb1c2;
    --white: #ffffff;
    --nav-muted: #d3c3c8;
    --placeholder: #a9a9a9;
    --avatar: #a0a0a0;
    --dot-active: #777777;
    --dot-idle: #c8c8c8;
    --footer-field: #d3d3d3;
    --submit-grey: #8e8e8e;
    --submit-lip: #cfcfcf;
    --ink: #111111;
  }
  * { margin: 0; padding: 0; box-sizing: border-box; }
  html, body { width: 998px; height: 1200px; overflow: hidden; }
  body {
    position: relative;
    font-family: "ABeeZee", sans-serif;
    background: var(--grey-body);
    color: var(--ink);
  }
  .abs { position: absolute; }

  .site-header { left: 0; top: 0; width: 998px; height: 75px; background: var(--mauve-dark); }
  .site-footer { left: 0; top: 938px; width: 998px; height: 262px; background: var(--mauve-dark); }
  .logo { font-size: 33px; color: var(--white); letter-spacing: 2px; line-height: 1; }
  .nav { display: flex; gap: 21px; font-size: 17.6px; color: var(--nav-muted); line-height: 1; }
  .nav .current { color: var(--white); }

  .hero { left: 0; top: 75px; width: 998px; height: 321px; background: var(--pink-hero); overflow: hidden; }
  .hero-art {
    left: 0; top: 29px; width: 190px; height: 260px;
    background: linear-gradient(90deg, var(--pink-deep) 0%, var(--pink-deep) 60%, var(--pink-hero) 100%);
  }
  .hero-title {
    right: 151px; top: 98px; text-align: right; white-space: nowrap;
    color: var(--white); font-size: 36px; line-height: 54px; font-weight: 400;
  }

  .section-title { font-size: 31px; line-height: 37px; font-weight: 400; white-space: nowrap; }
  .compare-title { left: 150px; top: 503px; }
  .reviews-title { right: 151px; top: 503px; text-align: right; }

  .field {
    background: var(--white); border-radius: 8px;
    font-size: 20px; color: var(--placeholder);
    display: flex; align-items: center; padding-left: 13px;
  }
  .btn {
    border-radius: 8px; color: var(--white); font-size: 24px;
    display: flex; align-items: center; justify-content: center;
  }
  .btn-compare {
    left: 149px; top: 770px; width: 321px; height: 47px;
    background: var(--button-berry);
    box-shadow: 0 8px 0 var(--button-lip);
  }

  .avatar { left: 530px; top: 613px; width: 120px; height: 120px; border-radius: 50%; background: var(--avatar); }
  .quote { left: 666px; top: 611px; font-size: 20px; line-height: 24.7px; white-space: nowrap; }
  .dots { left: 658px; top: 791px; display: flex; gap: 7px; }
  .dots span { width: 10px; height: 10px; border-radius: 50%; background: var(--dot-idle); }
  .dots .active { background: var(--dot-active); }

  .footer-about { left: 148px; top: 1016px; font-size: 16px; line-height: 18.5px; color: var(--white); white-space: nowrap; }
  .copyright { left: 150px; top: 1155px; font-size: 16px; color: var(--white); }
  .newsletter-title { left: 512px; top: 1013px; font-size: 22px; color: var(--white); }
  .field-email { left: 512px; top: 1058px; width: 335px; height: 47px; background: var(--footer-field); color: var(--placeholder); }
  .btn-submit {
    left: 512px; top: 1118px; width: 335px; height: 47px;
    background: var(--submit-grey);
    box-shadow: 0 8px 0 var(--submit-lip);
  }
</style>
</head>
<body>
  <header class="abs site-header">
    <div class="abs logo" style="left:148px; top:22px;">LOGO</div>
    <nav class="abs nav" style="left:539px; top:33px;">
      <span class="current">Home</span><span>About Us</span><span>Affiliate Program</span>
    </nav>
  </header>

  <section class="abs hero">
    <div class="abs hero-art" role="img" aria-label="Decorative home illustration"></div>
    <h1 class="abs hero-title">Welcome to the seller’s coner!<br>Find Your Perfect Listing Agent Today</h1>
  </section>

  <h2 class="abs section-title compare-title">Compare Top Realtors<br>in Your Area now!</h2>
  <div class="abs field" style="left:150px; top:613px; width:320px; height:47px;">Target Price</div>
  <div class="abs field" style="left:148px; top:685px; width:322px; height:46px;">Property’s zip code</div>
  <div class="abs btn btn-compare">Compare Selling Realtors</div>

  <h2 class="abs section-title reviews-title">See what Other<br>Sellers say!</h2>
  <div class="abs avatar" role="img" aria-label="Reviewer portrait"></div>
  <p class="abs quote">It is good It is good<br>It is good It is good<br>It is good It is good<br>It is good It is good<br>It is good It is good</p>
  <div class="abs dots"><span class="active"></span><span></span><span></span><span></span></div>

  <footer class="abs site-footer"></footer>
  <div class="abs logo" style="left:148px; top:962px;">LOGO</div>
  <nav class="abs nav" style="left:539px; top:974px;">
    <span class="current">Home</span><span>About Us</span><span>Affiliate Program</span>
  </nav>
  <p class="abs footer-about">Comp any de script ion Comp any de script i<br>on Comp any de script ion Comp any de scri<br>pt ion Comp any de script ion Co mp any de<br>script ion Comp any de script ion Comp anyd<br>escript ion Comp any de script ion Comp any<br>descript ion whweoh wioe hfweif lw wlkh fw<br>woefh weoif hiowhf iwhf wlwe f hw</p>
  <p class="abs copyright">Company Name @ 2016</p>
  <p class="abs newsletter-title">Get our free newsletter!</p>
  <div class="abs field field-email">Email adress</div>
  <div class="abs btn btn-submit">Submit</div>
</body>
</html>
```